Modern wordpress-enabled design wanted for translations agency serving large corporations

We are a translation agency and we only work for corporate clients and not private individuals. We are currently using the Marrow wordpress theme and an upload feature called quenbox. It is important that prospective clients can upload their file. So we need a cool design for that kind of feature. We offer different kinds of translations tailored to the needs or global corporations. Corporate communications translations, legal translations, financial translations, healthcare translations, financial translations, audit translations.

```html
<!DOCTYPE html>
<html lang="en">
<head>
<meta charset="utf-8">
<title>Translation Agency</title>
<link rel="stylesheet" href="https://fonts.googleapis.com/css2?family=Questrial&family=Open+Sans:ital,wght@0,400;0,600;0,700;1,400&family=Oswald:wght@500&display=swap">
<style>
:root{
  --green:#8cc13f;
  --green-dark:#76a82e;
  --blue:#45a6dc;
  --blue-dark:#2f8fc8;
  --blue-band:#4aa7dc;
  --text:#333;
  --muted:#555;
  --grey-bg:#ececec;
  --line:#d6d6d6;
  --white:#fff;
}
*{box-sizing:border-box;margin:0;padding:0}
html,body{width:721px;height:1200px;overflow:hidden;background:var(--white)}
body{position:relative;font-family:"Open Sans",Arial,sans-serif;color:var(--text)}
.abs{position:absolute}
a{color:inherit;text-decoration:none}

/* header */
.top-rule{left:0;top:0;width:721px;height:3px;background:var(--green)}
.brand{left:97px;top:14px;display:flex;align-items:center;gap:8px}
.brand-mark{width:40px;height:36px;border-radius:50%;background:var(--blue)}
.brand-name{font-family:"Questrial",sans-serif;font-size:20px;line-height:17px;color:#333;letter-spacing:1px}
.auth{top:16px;height:13px;font-size:7px;color:#fff;display:flex;align-items:center;justify-content:center}
.auth.login{left:555px;width:31px;background:var(--green)}
.auth.signup{left:591px;width:34px;background:var(--blue)}
.call-top{left:489px;top:38px;font-size:10px;color:#222}

/* nav */
.nav{left:0;top:62px;width:721px;height:28px;background:var(--green);border-bottom:2px solid var(--green-dark)}
.nav ul{list-style:none;position:absolute;left:91px;top:0;display:flex}
.nav li{height:28px;display:flex;align-items:center;justify-content:center;font-family:"Questrial",sans-serif;font-size:11px;color:#1f2d10;border-left:1px solid var(--green-dark)}
.nav li:first-child{border-left:0}
.nav li.active{background:var(--blue);color:#fff;border:1px solid #2f8fc8}

/* hero */
.hero{left:0;top:90px;width:721px;height:274px;background:linear-gradient(100deg,#b9c4cc 0%,#e6ecef 40%,#f3f5f6 60%,#c9d2d8 100%)}
.hero-caption{left:100px;top:302px;width:520px;height:48px;background:rgba(40,40,40,.65);display:flex;align-items:center;padding-left:10px}
.hero-caption h1{font-family:"Questrial",sans-serif;font-weight:400;font-size:18.5px;color:#fff}
.btn{display:flex;align-items:center;justify-content:center;font-size:8px}
.btn-green{background:var(--green);color:#1e2a10}
.btn-blue{background:var(--blue);color:#fff}
.btn-light{background:#eef5fa;color:#333;border:1px solid #cfe2ee}
.hero-cta{left:543px;top:316px;width:64px;height:20px;font-weight:700}

/* services */
.services{left:0;top:364px;width:721px;height:171px;background:var(--blue-band)}
.service{top:370px;height:158px;border:1px dashed rgba(255,255,255,.35);text-align:center;color:#fff}
.service.active{background:var(--blue-dark);border:0}
.service h2{font-family:"Questrial",sans-serif;font-weight:400;font-size:14.5px;color:#13324a;margin-top:18px;line-height:15px}
.service h2 small{display:block;font-size:10.5px}
.service .rule{width:28px;height:1px;background:rgba(255,255,255,.7);margin:13px auto 11px}
.service p{font-size:7px;font-style:italic;line-height:9px;padding:0 10px}
.service .btn{width:58px;height:18px;margin:10px auto 0}
.arrow{top:425px;width:14px;height:36px}

/* tabs */
.tab{top:564px;height:26px;display:flex;align-items:center;justify-content:center;font-size:9px;color:#222;background:#ddd}
.tab.active{background:var(--green)}
.tab-rule{left:99px;top:590px;width:521px;height:1px;background:var(--line)}
.upload-title{left:98px;top:597px;font-family:"Questrial",sans-serif;font-size:12.5px;color:#222}
.upload-title em{font-family:"Open Sans",sans-serif;font-size:7.5px}
.step-label{top:684px;width:160px;text-align:center;font-size:8px;font-weight:600;color:#222}
.steps-text{left:103px;top:702px;width:520px;font-size:7px;line-height:10px;color:#444}

/* contact banner */
.banner-photo{left:100px;top:750px;width:248px;height:64px;background:linear-gradient(90deg,#e9e9e9,#f7f7f7 60%,#dcdcdc)}
.banner-call{left:348px;top:750px;width:272px;height:64px;background:var(--blue);padding:12px 0 0 21px;color:#0d2131}
.banner-call .lead{font-family:"Oswald",sans-serif;font-weight:500;font-size:12px;line-height:14px}
.banner-call .num{font-family:"Oswald",sans-serif;font-weight:500;font-size:19px;letter-spacing:.5px}

/* info */
.info{left:0;top:845px;width:721px;height:235px;background:var(--grey-bg)}
.topics{left:100px;top:862px;width:220px;list-style:none}
.topics li{height:28px;display:flex;align-items:center;gap:9px;font-family:"Questrial",sans-serif;font-size:11px;color:#333;border-bottom:1px solid #dcdcdc}
.topics li.current{color:var(--blue)}
.topics i{width:12px;height:12px;background:var(--blue);display:inline-block;position:relative}
.topics i::after{content:"";position:absolute;left:3px;top:3px;width:4px;height:4px;border-right:1.5px solid #fff;border-top:1.5px solid #fff;transform:rotate(45deg)}
.topics li.current i{background:var(--green)}
.col-title{font-family:"Questrial",sans-serif;font-size:14px;color:#333}
.news{left:346px;top:888px;width:126px}
.news-item{padding-bottom:10px;margin-bottom:8px;border-bottom:1px solid #d8d8d8}
.news-item:last-child{border:0}
.news-item b{font-size:7px;display:block}
.news-item.fresh b{color:var(--blue)}
.news-item p{font-size:7px;font-style:italic;line-height:9px;color:#333}
.quote{left:493px;top:889px;width:130px;font-size:7.7px;font-style:italic;line-height:12.3px;color:#444}
.quote-name{left:493px;top:997px;font-size:7px;line-height:9px;color:#333}
.quote-name b{color:var(--blue);font-weight:600}

/* footer */
.foot-col{top:1096px;list-style:none;font-size:7px;color:#333;letter-spacing:.3px}
.foot-col li{height:15.5px;padding-left:10px;position:relative}
.foot-col li::before{content:"";position:absolute;left:0;top:2px;width:4px;height:4px;border-right:1px solid #777;border-top:1px solid #777;transform:rotate(45deg)}
.foot-col li.current{color:var(--green)}
.foot-brand{left:550px;top:1096px;font-family:"Questrial",sans-serif;font-size:10px;color:#333}
.socials{left:548px;top:1136px;display:flex;gap:2px}
.socials span{width:13px;height:13px;border-radius:50%;background:var(--blue)}
.socials span:nth-child(3){background:#666}
.copyright{left:0;top:1172px;width:721px;height:28px;background:var(--green);font-size:7px;color:#1e2a10;display:flex;align-items:center;justify-content:center}
</style>
</head>
<body>
<div class="abs top-rule"></div>
<div class="abs brand"><span class="brand-mark"></span><span class="brand-name">TRANSLATION<br>AGENCY</span></div>
<a class="abs auth login">Login</a>
<a class="abs auth signup">Sign Up</a>
<div class="abs call-top">Call Us Now : 0100-555-0142</div>

<nav class="abs nav">
  <ul>
    <li class="active" style="width:91px">Home</li>
    <li style="width:110px">About Us</li>
    <li style="width:110px">Language</li>
    <li style="width:111px">Services</li>
    <li style="width:109px">Contact Us</li>
  </ul>
</nav>

<div class="abs hero" role="img" aria-label="Photo of hands typing on a laptop beside a cluster of small national desk flags"></div>
<div class="abs hero-caption"><h1>The Highest Quality Of Our Translations for You!</h1></div>
<a class="abs btn btn-green hero-cta">READ MORE</a>

<section class="abs services"></section>
<svg class="abs arrow" style="left:69px" viewBox="0 0 14 36"><path d="M13 1 1 18l12 17" fill="none" stroke="#cfe8f6" stroke-width="1.2"/></svg>
<svg class="abs arrow" style="left:637px" viewBox="0 0 14 36"><path d="M1 1l12 17L1 35" fill="none" stroke="#cfe8f6" stroke-width="1.2"/></svg>
<article class="abs service" style="left:97px;width:123px"><h2>Same Day<small>Translations</small></h2><div class="rule"></div><p>Sed ut perspiciatis unde odmnis iste n error sit volup itatem accusa ehdfhntium do loremque laudantium, totadfgh.</p><a class="btn btn-light">Read More</a></article>
<article class="abs service active" style="left:226px;width:136px"><h2>Emergency<small>Assessments</small></h2><div class="rule"></div><p>Sed ut perspiciatis unde odmnis iste n error sit volup itatem accusa ehdfhntium do loremque laudantium, totadfgh.</p><a class="btn btn-light">Read More</a></article>
<article class="abs service" style="left:367px;width:124px"><h2>Weekend<small>Translations</small></h2><div class="rule"></div><p>Sed ut perspiciatis unde odmnis iste n error sit volup itatem accusa ehdfhntium do loremque laudantium, totadfgh.</p><a class="btn btn-light">Read More</a></article>
<article class="abs service" style="left:503px;width:123px"><h2>Overnight<small>Translations</small></h2><div class="rule"></div><p>Sed ut perspiciatis unde odmnis iste n error sit volup itatem accusa ehdfhntium do loremque laudantium, totadfgh.</p><a class="btn btn-light">Read More</a></article>

<div class="abs tab active" style="left:99px;width:141px">Upload Doc. And Get Offer</div>
<div class="abs tab" style="left:242px;width:91px">Why Choose Us</div>
<div class="abs tab" style="left:335px;width:64px">Features</div>
<div class="abs tab-rule"></div>
<h3 class="abs upload-title">Upload your document up here and get a personalized offer. <em>(Free and without obligation).</em></h3>

<svg class="abs" style="left:150px;top:628px" width="430" height="56" viewBox="0 0 430 56">
  <g fill="none" stroke-width="5">
    <path d="M35 4a24 21 0 1 1-14 39l-12 9 4-13A24 21 0 0 1 35 4z" stroke="#8cc13f"/>
    <path d="M207 4a24 21 0 1 1-14 39l-12 9 4-13A24 21 0 0 1 207 4z" stroke="#45a6dc"/>
    <path d="M387 4a24 21 0 1 1-14 39l-12 9 4-13A24 21 0 0 1 387 4z" stroke="#45a6dc"/>
  </g>
  <g font-family="Questrial,sans-serif" font-size="22" fill="#222" text-anchor="middle">
    <text x="36" y="33">1</text><text x="207" y="33">2</text><text x="387" y="33">3</text>
  </g>
  <g fill="#c8c8c8">
    <path d="M112 14h6l8 11-8 11h-6l8-11z"/><path d="M122 14h6l8 11-8 11h-6l8-11z"/>
    <path d="M290 14h6l8 11-8 11h-6l8-11z"/><path d="M300 14h6l8 11-8 11h-6l8-11z"/>
  </g>
</svg>
<div class="abs step-label" style="left:110px">Choose Target Language</div>
<div class="abs step-label" style="left:277px">Enter Your Translation Details</div>
<div class="abs step-label" style="left:457px">Change Your Document High</div>
<p class="abs steps-text">Lorem ipsum dolor sit amet, cons tuer adipiscing elit, se diam nonuummy nibh euismod. cons tuer adifghjiscing elit, werorem ipsum dolor sit ahdfhg dgfdghmons tuer adipiscing elit, se diam nonu use diam nonuummy nibh euismod. cons tuer adifghjmmyet.</p>

<div class="abs banner-photo" role="img" aria-label="Greetings written in many languages around a smiling office worker"></div>
<div class="abs banner-call"><div class="lead">YOU ARE FEE TO CONTACT AT OUR OFFICE</div><div class="num">CALL US NOW &nbsp;: &nbsp;100-555-0199</div></div>

<section class="abs info"></section>
<ul class="abs topics">
  <li><i></i>Translation Memory</li>
  <li><i></i>Health</li>
  <li><i></i>Terminology Management</li>
  <li class="current"><i></i>PROXY TRANSLATION</li>
  <li><i></i>Translation Services</li>
  <li><i></i>Financial Translation</li>
</ul>
<a class="abs btn btn-green" style="left:123px;top:1032px;width:60px;height:19px">Read More</a>

<h4 class="abs col-title" style="left:346px;top:867px">What's New?</h4>
<div class="abs news">
  <div class="news-item fresh"><b>2015-09-18</b><p>Lorem ipsum dolor sit amet, consectet ur adipiscing ipsum dolor</p></div>
  <div class="news-item"><b>2015-09-20</b><p>Lorem ipsum dolor sit amet, consectet ur adipiscing ipsum dolor</p></div>
  <div class="news-item"><b>2015-09-23</b><p>Lorem ipsum dolor sit amet, consectet ur adipiscing ipsum dolor</p></div>
</div>
<a class="abs btn btn-blue" style="left:347px;top:1031px;width:59px;height:18px;color:#123">View More</a>

<h4 class="abs col-title" style="left:493px;top:867px">Client's Testimonial</h4>
<p class="abs quote">“ Praesent vestibulum molestie lacus. Aenean nonummy hendrerit mauris. Phasellus porta. Fusce suscipit varius mi. Cum sociis penat vestibulum molestie lacus. Aenean nonummy hendrerit mauris. Phasellus porthasellus porta. Fusce suscipit varius mi.</p>
<div class="abs quote-name"><b>Dana Whitlow</b><br>- Manager (Northvale)</div>
<a class="abs btn btn-green" style="left:494px;top:1031px;width:59px;height:18px">View More</a>

<ul class="abs foot-col" style="left:99px"><li class="current">HOME</li><li>ABOUT US</li><li>CAREERS</li><li>SOLUTIONS</li></ul>
<ul class="abs foot-col" style="left:188px"><li>NEWS</li><li>CONTACT US</li><li>PRIACY POLICY</li><li>TERMS &amp; CONTITIONS</li></ul>
<ul class="abs foot-col" style="left:311px"><li>JOBS</li><li>RESOURCES</li><li>ASK AN EXPERT</li><li>NEWSLETTERS</li></ul>
<ul class="abs foot-col" style="left:415px"><li>CASE STUDIES</li><li>EXTRA SERVICES</li><li>OUR FACTS</li><li>URGENT TRANSLATION</li></ul>
<div class="abs foot-brand">Translation<br>Agency</div>
<div class="abs socials"><span></span><span></span><span></span><span></span></div>

<footer class="abs copyright">© 2015.&nbsp;<b>Translation Agency.</b>&nbsp;All rights reserved.</footer>
</body>
</html>
```